Business Card Design Project (on hold until logo completed)

Small Pharma Consulting Firm called "CopperVale" Pharma Solutions. Small business will be focused on ad hoc consulting projects. Business located near the beach so want to play off the location with the "ideas" so a "house of lights or ideas". The concept is to use a variety of experiences and expertise in the Pharma business to help clients use what they already know to tell a story and create ideas that better build customer solutions. Simplicity is key. We hire lots of consultants, create lots of data, conduct lots of research but we often get lost in all of it or do not have time to digest and analyze. We also get inwardly-focused. This small group will compress the information into simple chunks from a customer persective through a unique blend of skills and tools.
Updates

Project Deadline Extended
Reason: Logo is now completed so can begin business card design

Target Market(s)

Pharma Professionals, mostly marketing and analytics but could also be senior leadership

Industry/Entity Type

Business

Font styles to use
Sans Serif

Colors
00a990
fcca95
faa54b

Requirements
Must have
• logo with text
Nice to have
• Space for PO Box on 1 line, then city, state, zip on next line
Background should be white or tan/beige (to be eco-friendly, like the color of a brown paper bag)

```html
<!DOCTYPE html>
<html lang="en">
<head>
<meta charset="utf-8">
<title>CopperVale Pharma Solutions – Business Card</title>
<link rel="stylesheet" href="https://fonts.googleapis.com/css2?family=Lato:wght@400;700&display=swap">
<style>
  :root {
    --teal: #00a990;
    --teal-deep: #14937d;
    --orange: #faa54b;
    --peach: #fcca95;
    --ink: #222222;
    --muted: #4a4a4a;
    --card: #ffffff;
    --backdrop: #2f3e46;
  }
  * { box-sizing: border-box; margin: 0; padding: 0; }
  html, body {
    width: 1200px;
    height: 1000px;
    overflow: hidden;
    background: var(--backdrop);
    font-family: "Lato", Arial, sans-serif;
  }
  .card {
    position: absolute;
    left: 100px;
    top: 214px;
    width: 1000px;
    height: 572px;
    background: var(--card);
    border-radius: 4px;
    box-shadow: 0 18px 40px rgba(0, 0, 0, 0.35);
  }
  .holder {
    position: absolute;
    left: 46px;
    top: 46px;
    display: flex;
    align-items: baseline;
    gap: 22px;
  }
  .holder-name {
    font-size: 29px;
    font-weight: 700;
    color: var(--teal-deep);
  }
  .holder-role {
    font-size: 24px;
    font-weight: 400;
    color: var(--orange);
  }
  .brand {
    position: absolute;
    right: 150px;
    top: 125px;
    display: flex;
    align-items: center;
    gap: 24px;
  }
  .brand-dot {
    width: 72px;
    height: 72px;
    border-radius: 50%;
    background: var(--orange);
    flex: none;
  }
  .brand-name {
    display: flex;
    flex-direction: column;
    font-weight: 700;
    color: var(--teal-deep);
    text-transform: uppercase;
    line-height: 1.05;
  }
  .brand-name-main {
    font-size: 58px;
    letter-spacing: 1px;
  }
  .brand-name-sub {
    font-size: 29px;
    letter-spacing: 1.5px;
  }
  .contact {
    position: absolute;
    right: 78px;
    top: 300px;
    text-align: right;
    font-size: 28px;
    font-style: normal;
    color: var(--ink);
  }
  .contact-address {
    color: var(--muted);
    margin-bottom: 22px;
  }
  .contact-line { margin-bottom: 6px; }
  .label {
    font-weight: 700;
    color: var(--teal-deep);
    margin-right: 6px;
  }
  .label-gap { margin-left: 16px; }
  .contact-web {
    margin-top: 22px;
    color: var(--teal-deep);
  }
  .contact-web strong { font-weight: 700; }
</style>
</head>
<body>
  <article class="card">
    <header class="holder">
      <span class="holder-name">Name Here</span>
      <span class="holder-role">Project Manager</span>
    </header>

    <div class="brand">
      <span class="brand-dot" aria-hidden="true"></span>
      <span class="brand-name">
        <span class="brand-name-main">CopperVale</span>
        <span class="brand-name-sub">Pharma Solutions LLC</span>
      </span>
    </div>

    <address class="contact">
      <p class="contact-address">PO Box here, City, State Zip</p>
      <p class="contact-line"><span class="label">M</span>555-555-0100<span class="label label-gap">T</span>555-555-0199</p>
      <p class="contact-line"><span class="label">E</span>name@domain-name.com</p>
      <p class="contact-web">www.<strong>domain-name</strong>.com</p>
    </address>
  </article>
</body>
</html>
```